High-Class Professional Letterhead for a solo doctor's practice.

Please create a letterhead design that includes my logo, and options of my light blue/black color scheme and black and gold so I can choose between the two. I would like my Contact information on the top or bottom of the letterhead somewhere:
Celina Varga, M.D.
Hand and Upper Extremity Surgeon
4382 SW 58th Lane, Suite 305
Lakemont, FL 33490
Phone: (954) 555-0148
Fax: (800) 555-0172
www.cvargaortho.example

Also on the bottom of the letterhead, there should be 2 different versions:
one that is blank, and one that has a signature spot on the bottom so I can sign:
Celina Varga, M.D.
Board Certified Orthopaedic Hand Surgeon

I am going for classy/professional. I want other doctors and or lawyers to look at my letterhead and want to work with me. Again, professional, classy, clean. I do like black and gold but I could see what the blue like my other business card looks like too. Please do what most people do for letterheads--I'm not sure if the signature line should be on there? Or should be blank? I have no clue

Target Market(s)

Doctors and Lawyers

Industry/Entity Type

Medicine

Colors
0054AA
0677BA
7BADD7
CADEEF
E8F1F8

Requirements
Must have
• High class, professional, appealing

```html
<!DOCTYPE html>
<html lang="en">
<head>
<meta charset="utf-8">
<title>Celina Varga, M.D. — Letterhead</title>
<link rel="stylesheet" href="https://fonts.googleapis.com/css2?family=Jost:wght@400;500;600&family=Arimo:wght@400&display=swap">
<style>
  :root {
    --backdrop: #d8d0ca;
    --paper: #ffffff;
    --ink-dark: #262626;
    --gold: #c9a66b;
    --body-text: #454545;
    --contact-text: #2f2f2f;
    --watermark: #efefef;
    --signature-fill: #f1f1f1;
  }
  * { margin: 0; padding: 0; box-sizing: border-box; }
  html, body {
    width: 1012px; height: 1200px; overflow: hidden;
    background: var(--backdrop);
  }
  .letterhead {
    position: absolute; left: 86px; top: 15px;
    width: 840px; height: 1170px;
    background: var(--paper);
    overflow: hidden;
    box-shadow: 0 4px 14px rgba(0,0,0,0.18);
  }
  .letterhead__bands {
    position: absolute; inset: 0; width: 840px; height: 1170px;
  }
  .brand-seal {
    position: absolute; left: 48px; top: 42px;
    width: 178px; height: 178px; border-radius: 50%;
    background: var(--paper);
    border: 3px solid var(--gold);
    display: flex; align-items: center; justify-content: center;
    text-align: center;
  }
  .brand-seal__name {
    font-family: "Jost", sans-serif; font-weight: 500;
    font-size: 24px; line-height: 1.1; letter-spacing: 2px;
    color: var(--gold);
    text-transform: uppercase;
  }
  .contact {
    position: absolute; left: 362px; top: 62px;
    font-family: "Jost", sans-serif; font-size: 12.2px;
    font-style: normal;
    line-height: 19px; color: var(--contact-text);
  }
  .contact__name { color: var(--gold); font-weight: 600; }
  .contact__label { color: var(--gold); }
  .contact__divider { color: var(--gold); padding: 0 3px; }
  .watermark {
    position: absolute; left: 453px; top: 800px;
    width: 330px;
    font-family: "Jost", sans-serif; font-weight: 500;
    font-size: 96px; line-height: 1; color: var(--watermark);
    text-transform: uppercase; text-align: right;
  }
  .letter {
    position: absolute; left: 47px; top: 326px; width: 745px;
    font-family: "Arimo", sans-serif; font-size: 16.3px;
    line-height: 24px; color: var(--body-text);
  }
  .letter__recipient { margin-bottom: 16px; }
  .letter__paragraph { text-align: justify; hyphens: auto; }
  .letter__paragraph--second { margin-top: 26px; }
  .letter__paragraph--third { margin-top: 22px; }
  .letter__closing { margin-top: 16px; }
  .letter__signature {
    margin-top: 12px; width: 150px; height: 62px;
    background: var(--signature-fill); border-radius: 3px;
  }
</style>
</head>
<body>
  <main class="letterhead">
    <svg class="letterhead__bands" viewBox="0 0 840 1170" aria-hidden="true">
      <defs>
        <linearGradient id="goldSweep" x1="0" x2="1" y1="0" y2="0">
          <stop offset="0" stop-color="#b08d55"/>
          <stop offset="0.55" stop-color="#d9bb85"/>
          <stop offset="0.8" stop-color="#ead4a6"/>
          <stop offset="1" stop-color="#d2b27b"/>
        </linearGradient>
      </defs>
      <path class="band-dark-top" fill="var(--ink-dark)"
        d="M0,0 H840 V4 C600,6 380,42 200,100 C120,125 50,140 0,148 Z"/>
      <path class="band-gold-top" fill="url(#goldSweep)"
        d="M0,150 C50,142 120,127 200,102 C380,44 600,8 780,7 C600,15 380,52 200,116 C120,144 50,166 0,180 Z"/>
      <path class="band-dark-bottom" fill="var(--ink-dark)"
        d="M0,1100 C60,1150 160,1162 300,1157 C480,1150 620,1120 720,1119 C780,1119 815,1129 840,1140 V1170 H0 Z"/>
      <path class="band-gold-bottom" fill="url(#goldSweep)"
        d="M35,1112 C100,1138 200,1143 320,1138 C480,1128 620,1106 720,1105 C760,1105 790,1110 808,1116 C770,1112 740,1112 720,1113 C620,1118 480,1141 320,1149 C200,1154 100,1145 35,1112 Z"/>
    </svg>

    <div class="brand-seal">
      <span class="brand-seal__name">Varga<br>Hand</span>
    </div>

    <address class="contact">
      <div class="contact__name">Celina Varga, M.D.</div>
      <div>Hand and Upper Extremity Surgeon</div>
      <div>4382 SW 58th Lane, Suite 305 Lakemont, FL 33490</div>
      <div><span class="contact__label">Phone:</span> (954) 555-0148<span class="contact__divider">|</span><span class="contact__label">Fax:</span> (800) 555-0172<span class="contact__divider">|</span><span class="contact__label">Web:</span> www.cvargaortho.example</div>
    </address>

    <div class="watermark" aria-hidden="true">Varga<br>Hand</div>

    <article class="letter">
      <div class="letter__recipient">
        Mr/s<br>First Name and Last Name<br>Company Name<br>Address
      </div>
      <p class="letter__paragraph">Lorem Ipsum is simply dummy text of the printing and typesetting industry. Lorem Ipsum has been the industry's standard dummy text ever since the 1500s, when an unknown printer took a galley of type and scrambled it to make a type specimen book. It has survived not only five centuries, but also the leap into electronic typesetting, remaining essentially unchanged. It was popularised in the 1960s with the release of Letraset sheets containing Lorem Ipsum passages.</p>
      <p class="letter__paragraph letter__paragraph--second">he standard chunk of Lorem Ipsum used since the 1500s is reproduced below for those interested. Sections 1.10.32 and 1.10.33 from "de Finibus Bonorum et Malorum" by Cicero are also reproduced in their exact original form, accompanied by English versions from the 1914 translation by H. Rackham. Lorem ipsum dolor sit amet, consectetur adipiscing elit, sed do eiusmod tempor incididunt ut labore et dolore magna aliqua.</p>
      <p class="letter__paragraph letter__paragraph--third">It is a long established fact that a reader will be distracted by the readable content of a page when looking at its layout. The point of using Lorem Ipsum is that it has a more-or-less normal distribution of letters, as opposed to using 'Content here, content here', making it look like readable English. Many desktop publishing packages and web page editors now .</p>
      <p class="letter__closing">Your Sincerely,</p>
      <div class="letter__signature" role="img" aria-label="Handwritten signature"></div>
    </article>
  </main>
</body>
</html>
```